VARSEK MOBILE APP RE-DESIGN - MINIMALISTIC AND CLEAN DESIGN

We are looking for a design that is minimalistic, clean, modern and appealing to millennials...
IMPORTANT: This is NOT a logo design nor a website design... This is for a mobile App Design. You can download our app on iOS or Android: "VARSEK eLINKUP"

We are attaching our new logo and some apps that we like the design, colors, shadows, 3d effects, style, etc...

For content, you can check our website: www.varsek-app.example

Please feel free to ask questions, it's very important that you understand the project. Thank you

Also, check out this website...we do like the design and colors: https://brontil-demo.example/
Updates

This is not for a logo design... this is for a mobile app design.... please download our app on iOS: VARSEK eLINKUP... THANK YOU

Target Market(s)

20 - 35
60% Male 40 Female

Requirements
Must have
• great graphics, color shadows for 3d effects, great colors with transparency, IMPORTANT: CLEAN DESIGN, Minimalistic.

```html
<!DOCTYPE html>
<html lang="en">
<head>
<meta charset="utf-8">
<title>VARSEK — Splash Screen</title>
<link href="https://fonts.googleapis.com/css2?family=Open+Sans:wght@400;600&display=swap" rel="stylesheet">
<style>
  :root {
    --canvas-bg: #e8ebee;
    --screen-bg: #5330f6;
    --screen-bg-light: #6a48f9;
    --status-ink: #ffffff;
    --brand-square-top: #2fa3e0;
    --brand-square-bottom: #1570c0;
    --brand-name: #3fb6f2;
    --bar-outline: #2a2350;
    --bar-start: #b13cf0;
    --bar-end: #8a8cff;
  }
  * { box-sizing: border-box; margin: 0; padding: 0; }
  html, body {
    width: 1200px;
    height: 900px;
    overflow: hidden;
    background: var(--canvas-bg);
    font-family: "Open Sans", Arial, sans-serif;
  }
  .stage {
    position: relative;
    width: 1200px;
    height: 900px;
  }
  .screen {
    position: absolute;
    background: var(--screen-bg);
    overflow: hidden;
  }
  .screen--ios {
    left: 148px; top: 112px;
    width: 322px; height: 700px;
    border-radius: 40px;
  }
  .screen--android {
    left: 728px; top: 112px;
    width: 332px; height: 696px;
    border-radius: 6px;
    background: linear-gradient(160deg, var(--screen-bg-light) 0%, var(--screen-bg) 45%);
  }
  .status-bar {
    position: absolute;
    top: 0; left: 0; right: 0;
    height: 36px;
    color: var(--status-ink);
    font-size: 12px;
    font-weight: 600;
    display: flex;
    align-items: center;
    justify-content: space-between;
    padding: 0 26px;
  }
  .screen--android .status-bar {
    justify-content: flex-end;
    gap: 8px;
    height: 32px;
    padding: 0 8px;
    font-weight: 400;
    font-size: 11px;
  }
  .status-icons { display: flex; gap: 5px; align-items: center; }
  .home-indicator {
    position: absolute;
    bottom: 8px; left: 50%;
    width: 116px; height: 4px;
    margin-left: -58px;
    border-radius: 2px;
    background: #ffffff;
  }
  .splash {
    position: absolute;
    left: 0; right: 0;
    top: 258px;
    display: flex;
    flex-direction: column;
    align-items: center;
  }
  .brand-square {
    width: 154px; height: 154px;
    border-radius: 14px;
    background: linear-gradient(150deg, var(--brand-square-top), var(--brand-square-bottom));
    box-shadow: 0 8px 18px rgba(20, 10, 90, 0.35);
  }
  .brand-name {
    margin-top: 14px;
    font-size: 35px;
    font-weight: 400;
    letter-spacing: 1px;
    color: var(--brand-name);
    line-height: 1.1;
  }
  .loading-bar {
    margin-top: 44px;
    width: 242px; height: 24px;
    border: 3px solid var(--bar-outline);
    border-radius: 12px;
    padding: 3px;
    background: #3b2d9a;
  }
  .loading-fill {
    width: 100%; height: 100%;
    border-radius: 8px;
    background: linear-gradient(90deg, var(--bar-start), var(--bar-end));
    box-shadow: inset 0 2px 2px rgba(255,255,255,0.35);
  }
</style>
</head>
<body>
<main class="stage">

  <section class="screen screen--ios" aria-label="VARSEK splash screen, iOS">
    <div class="status-bar">
      <span class="status-time">9:41</span>
      <span class="status-icons">
        <svg width="18" height="10" viewBox="0 0 18 10" aria-hidden="true"><rect x="0" y="7" width="3" height="3" fill="#fff"/><rect x="4" y="5" width="3" height="5" fill="#fff"/><rect x="8" y="3" width="3" height="7" fill="#fff"/><rect x="12" y="0" width="3" height="10" fill="#fff"/></svg>
        <svg width="14" height="10" viewBox="0 0 14 10" aria-hidden="true"><path d="M7 9.5l2-2.4a3 3 0 0 0-4 0z M2.6 5a6.5 6.5 0 0 1 8.8 0l-1.2 1.3a4.7 4.7 0 0 0-6.4 0z M0.3 2.6a9.8 9.8 0 0 1 13.4 0L12.5 3.9a8 8 0 0 0-11 0z" fill="#fff"/></svg>
        <svg width="24" height="11" viewBox="0 0 24 11" aria-hidden="true"><rect x="0.5" y="0.5" width="20" height="10" rx="3" fill="none" stroke="#fff" opacity="0.6"/><rect x="2" y="2" width="17" height="7" rx="1.5" fill="#fff"/><rect x="21.5" y="3.5" width="1.5" height="4" rx="0.7" fill="#fff" opacity="0.6"/></svg>
      </span>
    </div>
    <div class="splash">
      <div class="brand-square" aria-hidden="true"></div>
      <h1 class="brand-name">VARSEK</h1>
      <div class="loading-bar" role="progressbar" aria-label="Loading"><div class="loading-fill"></div></div>
    </div>
    <div class="home-indicator"></div>
  </section>

  <section class="screen screen--android" aria-label="VARSEK splash screen, Android">
    <div class="status-bar">
      <span class="status-icons">
        <svg width="10" height="9" viewBox="0 0 10 9" aria-hidden="true"><path d="M0 0h10L5 9z" fill="#fff"/></svg>
        <svg width="9" height="9" viewBox="0 0 9 9" aria-hidden="true"><path d="M9 0v9H0z" fill="#fff"/></svg>
        <svg width="7" height="10" viewBox="0 0 7 10" aria-hidden="true"><rect x="2" y="0" width="3" height="1.5" fill="#fff"/><rect x="0" y="1.5" width="7" height="8.5" rx="1" fill="#fff"/></svg>
      </span>
      <span class="status-time">12:00</span>
    </div>
    <div class="splash">
      <div class="brand-square" aria-hidden="true"></div>
      <h1 class="brand-name">VARSEK</h1>
      <div class="loading-bar" role="progressbar" aria-label="Loading"><div class="loading-fill"></div></div>
    </div>
  </section>

</main>
</body>
</html>
```